KORVELTA Corporate Business Card

Modern business card design for company which focuses in the areas of Staffing, IT Consulting & Data Services. Please note: We are no longer using the IT subscript on the logo. All designs should have IT subscript removed.
Website: www.korveltait.example

```html
<!DOCTYPE html>
<html lang="en">
<head>
<meta charset="utf-8">
<title>KORVELTA Corporate Business Card</title>
<link rel="stylesheet" href="https://fonts.googleapis.com/css2?family=Roboto:ital,wght@0,400;0,700;1,400&display=swap">
<style>
  :root {
    --backdrop: #26282b;
    --card-white: #ffffff;
    --card-shade: #eef1f5;
    --brand-blue: #4a86c8;
    --deep-blue: #2e5a94;
    --navy: #1f3f73;
    --text-blue: #2b4f86;
    --rule: #3a5c92;
  }
  * { box-sizing: border-box; margin: 0; padding: 0; }
  html, body { width: 1200px; height: 985px; overflow: hidden; }
  body {
    background: var(--backdrop);
    font-family: "Roboto", Arial, sans-serif;
    position: relative;
  }
  .card {
    position: absolute;
    width: 620px;
    height: 355px;
    border-radius: 3px;
    overflow: hidden;
    box-shadow: 0 12px 30px rgba(0,0,0,.55);
  }

  /* Back side */
  .card--back {
    left: 500px; top: 70px;
    background: var(--deep-blue);
  }
  .back-pattern {
    position: absolute; inset: 0;
    background: linear-gradient(120deg, #23497d 0%, #2e5a94 55%, #4a82c4 100%);
  }
  .back-wordmark {
    position: absolute;
    left: 250px; top: 205px;
    display: flex; align-items: center; gap: 12px;
    color: var(--card-white);
    font-weight: 700;
    font-size: 46px;
    letter-spacing: 2px;
  }
  .back-wordmark .mark-square {
    width: 34px; height: 34px; background: var(--card-white);
  }

  /* Front side */
  .card--front {
    left: 80px; top: 520px;
    background: linear-gradient(135deg, var(--card-white) 40%, var(--card-shade) 100%);
  }
  .front-wordmark {
    position: absolute; left: 34px; top: 28px;
    display: flex; align-items: center; gap: 10px;
    color: var(--brand-blue);
    font-weight: 700; font-size: 38px; letter-spacing: 1.5px;
  }
  .front-wordmark .mark-square {
    width: 26px; height: 26px; background: var(--brand-blue);
  }
  .holder { position: absolute; left: 44px; top: 118px; }
  .holder-name { color: var(--brand-blue); font-weight: 700; font-size: 25px; }
  .holder-role { color: var(--text-blue); font-style: italic; font-size: 15px; margin-top: 1px; }
  .contacts { position: absolute; left: 44px; top: 186px; list-style: none; }
  .contacts li {
    display: flex; align-items: center; gap: 10px;
    color: var(--text-blue); font-style: italic; font-size: 16px;
    line-height: 24px;
  }
  .contacts svg { width: 14px; height: 14px; fill: var(--brand-blue); flex: none; }
  .contacts .accent { color: var(--brand-blue); }
  .divider {
    position: absolute; left: 40px; right: 40px; top: 268px;
    height: 1px; background: var(--rule);
  }
  .address {
    position: absolute; left: 44px; top: 278px;
    color: var(--text-blue); font-style: italic; font-size: 16px;
  }
  .base-band {
    position: absolute; left: 0; right: 0; bottom: 0; height: 12px;
    background: var(--brand-blue);
  }
  .base-band::before {
    content: ""; position: absolute; left: 0; top: 0; bottom: 0; width: 70px;
    background: var(--navy);
    border-right: 5px solid var(--card-white);
  }
</style>
</head>
<body>

  <section class="card card--back">
    <div class="back-pattern" role="img" aria-label="Repeating tiled brand pattern in shades of blue"></div>
    <div class="back-wordmark"><span class="mark-square"></span>KORVELTA</div>
  </section>

  <section class="card card--front">
    <div class="front-wordmark"><span class="mark-square"></span>KORVELTA</div>

    <div class="holder">
      <p class="holder-name">Marek Holloway</p>
      <p class="holder-role">Manager</p>
    </div>

    <ul class="contacts">
      <li>
        <svg viewBox="0 0 24 24"><path d="M6.6 10.8a15.1 15.1 0 0 0 6.6 6.6l2.2-2.2c.3-.3.7-.4 1-.2 1.1.4 2.3.6 3.6.6.6 0 1 .4 1 1V20c0 .6-.4 1-1 1A17 17 0 0 1 3 4c0-.6.4-1 1-1h3.5c.6 0 1 .4 1 1 0 1.3.2 2.5.6 3.6.1.3 0 .7-.2 1z"/></svg>
        555-014-2760
      </li>
      <li>
        <svg viewBox="0 0 24 24"><path d="M2 5h20v14H2z M2 5l10 8 10-8" fill="none" stroke="#4a86c8" stroke-width="2"/></svg>
        contactus@korveltait.example
      </li>
      <li>
        <svg viewBox="0 0 24 24"><circle cx="12" cy="12" r="9" fill="none" stroke="#4a86c8" stroke-width="2"/><path d="M3 12h18M12 3c3 3 3 15 0 18M12 3c-3 3-3 15 0 18" fill="none" stroke="#4a86c8" stroke-width="1.6"/></svg>
        <span>www.<span class="accent">korveltait</span>.example</span>
      </li>
    </ul>

    <div class="divider"></div>
    <p class="address">418 Larkspur Rd., Brennford, OH 45990</p>
    <div class="base-band"></div>
  </section>

</body>
</html>
```